Spurs, Steers & Supper

Design for a 5'x10' Banner. Country western theme for an event with young men and women (ages 21-24).

• Attached is the invitation that goes with the event. I do not need that date, times, names etc on the banner

```html
<!DOCTYPE html>
<html lang="en">
<head>
<meta charset="utf-8">
<title>Spurs, Steers &amp; Supper – Event Banner</title>
<link rel="stylesheet" href="https://fonts.googleapis.com/css2?family=Rye&display=swap">
<style>
  :root {
    --canvas-bg: #e8e8e8;
    --kraft: #c89c73;
    --kraft-light: #d6ae88;
    --kraft-dark: #a97d55;
    --ink: #1b1714;
    --ink-soft: rgba(27, 23, 20, 0.28);
    --ink-faint: rgba(27, 23, 20, 0.14);
    --photo-dark: #2e2119;
    --photo-warm: #9a5a36;
    --photo-light: #dccab0;
    --photo-red: #a52a22;
  }
  html, body {
    margin: 0;
    padding: 0;
    width: 1200px;
    height: 1200px;
    overflow: hidden;
    background: var(--canvas-bg);
  }
  .canvas {
    position: relative;
    width: 1200px;
    height: 1200px;
  }
  .banner {
    position: absolute;
    left: 325px;
    top: 50px;
    width: 550px;
    height: 1100px;
    overflow: hidden;
    background-color: var(--kraft);
    background-image:
      radial-gradient(circle at 12% 22%, var(--ink-soft) 0 2px, transparent 3px),
      radial-gradient(circle at 84% 31%, var(--ink-soft) 0 3px, transparent 4px),
      radial-gradient(circle at 7% 58%, var(--ink-soft) 0 2px, transparent 3px),
      radial-gradient(circle at 93% 62%, var(--ink-soft) 0 2px, transparent 3px),
      radial-gradient(circle at 20% 68%, var(--ink-soft) 0 3px, transparent 4px),
      radial-gradient(circle at 76% 70%, var(--ink-soft) 0 2px, transparent 3px),
      radial-gradient(circle at 9% 40%, var(--ink-faint) 0 14px, transparent 22px),
      radial-gradient(circle at 90% 45%, var(--ink-faint) 0 16px, transparent 26px),
      radial-gradient(circle at 15% 75%, var(--ink-faint) 0 18px, transparent 30px),
      radial-gradient(circle at 88% 25%, var(--ink-faint) 0 12px, transparent 20px),
      radial-gradient(circle at 3px 3px, var(--ink-faint) 0 1px, transparent 1.5px),
      radial-gradient(ellipse at 50% 42%, var(--kraft-light), var(--kraft) 55%, var(--kraft-dark));
    background-size: auto, auto, auto, auto, auto, auto, auto, auto, auto, auto, 17px 23px, auto;
  }
  .corner-bars {
    position: absolute;
    top: 30px;
    width: 62px;
  }
  .corner-bars--left { left: 0; }
  .corner-bars--right { right: 0; }
  .corner-bars span {
    display: block;
    height: 24px;
    margin-bottom: 14px;
    background: var(--ink);
    border-radius: 0 6px 6px 0;
  }
  .corner-bars--right span { border-radius: 6px 0 0 6px; }
  .emblem-circle {
    position: absolute;
    left: 120px;
    top: -70px;
    width: 310px;
    height: 310px;
    border-radius: 50%;
    background: var(--ink);
    box-shadow: inset 0 0 0 14px var(--ink), inset 0 0 0 18px var(--kraft);
  }
  .title-plate {
    position: absolute;
    left: 38px;
    top: 285px;
    width: 474px;
    height: 430px;
    box-sizing: border-box;
    border: 14px solid var(--ink);
    border-radius: 34px;
    background: rgba(214, 174, 136, 0.35);
  }
  .title-plate::before {
    content: "";
    position: absolute;
    inset: 8px;
    border: 4px solid var(--ink);
    border-radius: 22px;
  }
  .event-title {
    position: absolute;
    left: 0;
    top: 312px;
    width: 550px;
    margin: 0;
    text-align: center;
    font-family: "Rye", serif;
    font-weight: 400;
    color: var(--ink);
    line-height: 1.08;
  }
  .event-title span { display: block; }
  .event-title .line-1 { font-size: 96px; }
  .event-title .line-2 { font-size: 96px; }
  .event-title .line-3 { font-size: 74px; margin-top: 10px; }
  .food-photo {
    position: absolute;
    left: 0;
    bottom: 0;
    width: 550px;
    height: 330px;
  }
</style>
</head>
<body>
<div class="canvas">
  <section class="banner" aria-label="Spurs, Steers &amp; Supper event banner">
    <div class="corner-bars corner-bars--left"><span></span><span></span><span></span></div>
    <div class="corner-bars corner-bars--right"><span></span><span></span><span></span></div>
    <div class="emblem-circle" aria-hidden="true"></div>

    <div class="title-plate" aria-hidden="true"></div>
    <h1 class="event-title">
      <span class="line-1">SPURS,</span>
      <span class="line-2">STEERS</span>
      <span class="line-3">&amp; SUPPER</span>
    </h1>

    <svg class="food-photo" viewBox="0 0 550 330" role="img" aria-label="Photograph of a barbecue spread: grilled skewers, roasted peppers, eggplant, potatoes and dipping sauces on flatbread">
      <defs>
        <linearGradient id="foodBase" x1="0" y1="0" x2="1" y2="0.6">
          <stop offset="0" stop-color="var(--photo-dark)"/>
          <stop offset="0.3" stop-color="var(--photo-warm)"/>
          <stop offset="0.55" stop-color="var(--photo-light)"/>
          <stop offset="0.78" stop-color="var(--photo-warm)"/>
          <stop offset="1" stop-color="var(--photo-dark)"/>
        </linearGradient>
        <radialGradient id="pepperGlow" cx="0.78" cy="0.45" r="0.25">
          <stop offset="0" stop-color="var(--photo-red)" stop-opacity="0.8"/>
          <stop offset="1" stop-color="var(--photo-red)" stop-opacity="0"/>
        </radialGradient>
        <radialGradient id="sauceGlow" cx="0.4" cy="0.2" r="0.15">
          <stop offset="0" stop-color="var(--photo-red)" stop-opacity="0.7"/>
          <stop offset="1" stop-color="var(--photo-red)" stop-opacity="0"/>
        </radialGradient>
      </defs>
      <path d="M0 48 Q30 48 50 20 L150 20 Q170 20 178 42 L340 42 Q350 10 380 10 L440 10 Q470 10 478 38 L550 38 L550 330 L0 330 Z" fill="var(--ink)"/>
      <path d="M0 62 Q38 62 58 34 L142 34 Q160 34 166 56 L350 56 Q360 24 386 24 L434 24 Q460 24 466 52 L550 52 L550 330 L0 330 Z" fill="url(#foodBase)"/>
      <rect x="0" y="0" width="550" height="330" fill="url(#pepperGlow)"/>
      <rect x="0" y="0" width="550" height="330" fill="url(#sauceGlow)"/>
      <path d="M0 312 Q275 276 550 312 L550 330 L0 330 Z" fill="var(--ink)"/>
    </svg>
  </section>
</div>
</body>
</html>
```